Flyer Design Project

I need to create a flyer to advertise an Luxury Self Catering Apartment Complex in a Ski Resort in Europe. The development offers luxury accommodation to those who are on a budget.

Below is what needs to be included and a basic layout design idea i had that can be changed. The information is important. Hoping to get it on a flyer sized 21.6 x 14 cm

Title - 'Luxury Self Catering Ski Apartments For Rent'
Sub Title - 'Located 200m from Gondola, Restaurants and Bars'

Studio - Sleeps 1-2 - From only £200 per week
1 Bed - Sleeps 2-4 - From only £250 per week
2 Bed - Sleeps 4-6 - From only £350 per week

Image 1 Image 2 Image 3

- Fully Furnished Modern, Spacious & Comfortable Apartments
- Fully Staffed Development (Reception, Bar + Daily Cleaning)
- Family friendly & suitable for children of all ages

(Twitter Icon) @snowlarkchalets
E-mail - snowlarkchalets@mailvora.co.uk
Telephone - +44 (0) 7811 302 684

Target Market(s)

Our target market is very wide. We are trying to attract students, couples and families who are skiing on a budget.

Industry/Entity Type

Accommodation

Requirements
Must have
• The text contained in 'task description' is important but i'd like to be led on design. Size of around 21.6 x 14cm is important and i'd like the 3 images below (hopefully someone can get of the date and time in orange bottom right of all pics)

http://i2217.picvaultra.com/albums/kq412/tmwimages/Bansko/699_00_640_zpsd7b2ba81.jpeg

http://i2217.picvaultra.com/albums/kq412/tmwimages/Bansko/a_02_zps7503dd10.jpeg

http://i2217.picvaultra.com/albums/kq412/tmwimages/Bansko/699_08_640_zps2f11bf21.jpeg

```html
<!DOCTYPE html>
<html lang="en">
<head>
<meta charset="utf-8">
<title>Luxury Self Catering Ski Apartments For Rent – Flyer</title>
<link href="https://fonts.googleapis.com/css2?family=Oswald:wght@600&family=Crimson+Text:ital,wght@1,400;1,600&family=Arimo:ital,wght@0,400;0,700;1,700&display=swap" rel="stylesheet">
<style>
  :root {
    --stage: #606163;
    --navy: #0b2a4a;
    --blue: #1279b8;
    --cyan: #2fb6e6;
    --ink: #0a0c10;
    --panel: #101318;
    --white: #ffffff;
    --yellow: #ffd21a;
    --phone-red: #d4252a;
    --caption: #e8eef3;
  }
  * { margin: 0; padding: 0; box-sizing: border-box; }
  html, body { width: 1200px; height: 807px; overflow: hidden; }
  body { background: var(--stage); position: relative; font-family: "Arimo", Arial, sans-serif; }

  .flyer {
    position: absolute; left: 365px; top: 18px;
    width: 470px; height: 770px;
    background: var(--ink);
    overflow: hidden;
  }

  /* Header */
  .header { position: absolute; left: 0; top: 0; width: 470px; height: 150px; z-index: 1; }
  .header svg { position: absolute; left: 0; top: 0; }
  .title {
    position: absolute; left: -40px; right: -40px; top: 14px;
    text-align: center; color: var(--white); white-space: nowrap;
    font-family: "Oswald", "Arial Narrow", sans-serif; font-weight: 600;
    font-size: 28px; line-height: 36px; letter-spacing: -0.3px;
    transform: scaleX(0.86);
    text-shadow: 0 2px 3px rgba(0,0,0,.45);
  }
  .subtitle {
    position: absolute; left: 0; right: 0; top: 58px;
    text-align: center; color: var(--white); white-space: nowrap;
    font-family: "Crimson Text", Georgia, serif; font-style: italic; font-weight: 600;
    font-size: 22px; line-height: 28px;
  }
  .subtitle .dark { color: var(--navy); }

  /* Main photo */
  .hero-photo {
    position: absolute; left: 0; top: 118px; width: 470px; height: 347px;
    background: linear-gradient(180deg, #e9eaec 0%, #cfd1d3 38%, #8c7a66 62%, #5a4a3c 100%);
    z-index: 0;
  }

  /* Price rows */
  .rates { position: absolute; left: 0; top: 465px; width: 470px; }
  .rate {
    position: relative; height: 28px;
    background: linear-gradient(180deg, #1a1d22, #07080a);
    border-bottom: 2px solid var(--cyan);
    display: flex; align-items: center;
    font-style: italic; font-weight: 700; color: var(--white); font-size: 17px;
  }
  .rate-tab {
    width: 108px; height: 100%;
    background: linear-gradient(180deg, #48c8f2, #1792c9);
    clip-path: polygon(0 0, 82% 0, 100% 100%, 0 100%);
    padding-left: 8px; display: flex; align-items: center;
    font-size: 17px;
  }
  .rate-detail { padding-left: 22px; white-space: nowrap; }
  .rate-detail .price { color: var(--yellow); }

  /* Features */
  .features {
    position: absolute; left: 0; top: 550px; width: 470px; height: 158px;
    background:
      radial-gradient(ellipse 70% 55% at 50% 40%, rgba(30,130,200,.75), rgba(10,40,80,.35) 60%, transparent 80%),
      var(--panel);
    display: flex; justify-content: space-around; padding: 6px 6px 0;
  }
  .feature { width: 148px; text-align: center; }
  .feature-photo {
    width: 100px; height: 100px; margin: 0 auto; border-radius: 50%;
    border: 4px solid #e6e9ec;
    box-shadow: 0 0 0 2px #8a9096, 0 3px 6px rgba(0,0,0,.6);
  }
  .photo-building { background: linear-gradient(180deg, #e4e6e8 0%, #b9b2a6 45%, #6a5646 100%); }
  .photo-lounge { background: linear-gradient(160deg, #3a2a20 0%, #6b4a30 45%, #2a1c14 100%); }
  .photo-bedroom { background: linear-gradient(160deg, #c99a5c 0%, #f0e0c0 50%, #7a5532 100%); }
  .feature-text { margin-top: 6px; color: var(--caption); font-size: 11px; line-height: 13px; }

  /* Contact footer */
  .contact {
    position: absolute; left: 0; top: 708px; width: 470px; height: 62px;
    background: linear-gradient(180deg, #16191e, #050607);
    border-top: 1px solid #2a2e34;
  }
  .contact-list { position: absolute; left: 12px; top: 11px; list-style: none; }
  .contact-list li {
    display: flex; align-items: center; gap: 7px;
    color: var(--yellow); font-size: 13px; height: 20px; white-space: nowrap;
  }
  .contact-dot {
    width: 13px; height: 13px; border-radius: 50%;
    background: linear-gradient(180deg, #7fd6f5, #1a8fc8);
  }
  .divider { position: absolute; left: 236px; top: 6px; width: 1px; height: 50px; background: #3a3f46; }
  .phone {
    position: absolute; left: 250px; top: 11px;
    display: flex; align-items: center; gap: 10px;
    color: var(--yellow); font-weight: 700; font-size: 18px; white-space: nowrap;
  }
</style>
</head>
<body>
  <article class="flyer">
    <div class="hero-photo" role="img" aria-label="Photograph of the stone and white-rendered apartment building with balconies and mountains behind"></div>

    <header class="header">
      <svg width="470" height="150" viewBox="0 0 470 150" aria-hidden="true">
        <defs>
          <linearGradient id="headerBlue" x1="0" y1="0" x2="0" y2="1">
            <stop offset="0" stop-color="#0d5f98"/>
            <stop offset="0.55" stop-color="#1c9ad6"/>
            <stop offset="1" stop-color="#3cc3ef"/>
          </linearGradient>
        </defs>
        <path d="M0 0 H470 V118 C360 100 230 100 120 116 C70 123 30 128 0 132 Z" fill="url(#headerBlue)"/>
        <path d="M0 132 C30 128 70 123 120 116 C230 100 360 100 470 118 V126 C360 110 230 112 120 124 C70 130 30 136 0 140 Z" fill="#ffffff"/>
      </svg>
      <h1 class="title">Luxury Self Catering Ski Apartments For Rent</h1>
      <p class="subtitle">Located 200m from Gondola, <span class="dark">Restaurants and Bars</span></p>
    </header>

    <section class="rates">
      <div class="rate"><span class="rate-tab">Studio</span><span class="rate-detail">Sleeps 1-2 &nbsp;- &nbsp;<span class="price">From only £200 per week</span></span></div>
      <div class="rate"><span class="rate-tab">1 Bed</span><span class="rate-detail">Sleeps 2-4 &nbsp;- &nbsp;<span class="price">From only £250 per week</span></span></div>
      <div class="rate"><span class="rate-tab">2 Bed</span><span class="rate-detail">Sleeps 4-6 &nbsp;- &nbsp;<span class="price">From only £350 per week</span></span></div>
    </section>

    <section class="features">
      <div class="feature">
        <div class="feature-photo photo-building" role="img" aria-label="Photograph of the apartment building exterior"></div>
        <p class="feature-text">Fully Furnished Modern,<br>Spacious &amp; Comfortable<br>Apartments</p>
      </div>
      <div class="feature">
        <div class="feature-photo photo-lounge" role="img" aria-label="Photograph of a furnished apartment living area"></div>
        <p class="feature-text">Fully Staffed Development<br>(Reception, Bar + Daily<br>Cleaning)</p>
      </div>
      <div class="feature">
        <div class="feature-photo photo-bedroom" role="img" aria-label="Photograph of an apartment bedroom"></div>
        <p class="feature-text">Family friendly &amp;<br>suitable for children of<br>all ages</p>
      </div>
    </section>

    <footer class="contact">
      <ul class="contact-list">
        <li><span class="contact-dot"></span>@snowlarkchalets</li>
        <li><span class="contact-dot"></span>snowlarkchalets@mailvora.co.uk</li>
      </ul>
      <span class="divider"></span>
      <div class="phone">
        <svg width="22" height="22" viewBox="0 0 24 24" aria-hidden="true">
          <path fill="var(--phone-red)" d="M6.6 10.8c1.4 2.8 3.8 5.1 6.6 6.6l2.2-2.2c.3-.3.7-.4 1-.2 1.1.4 2.3.6 3.6.6.6 0 1 .4 1 1V20c0 .6-.4 1-1 1C10.6 21 3 13.4 3 4c0-.6.4-1 1-1h3.5c.6 0 1 .4 1 1 0 1.3.2 2.5.6 3.6.1.3 0 .7-.2 1l-2.3 2.2z"/>
        </svg>
        <span>+44 (0) 7811 302 684</span>
      </div>
    </footer>
  </article>
</body>
</html>
```